Corporate Identity Pack - LetterHead, Business Card, Envelope

We are looking for a clean, professional, and visually connected corporate identity set for our company "MERIDA CARE" (Cleaning, Gardening, and Pest Control services).

The pack must include:

Business Card (front and back)
Envelope with recipient window on the right side (22x11)
A4 Letterhead

We provide:
Our final logo (PNG)
Three design references (Inspiration1, Inspiration2, Inspiration3) to spark ideas — but you are absolutely free to propose your own creative solutions based on these concepts.

What we want:
A clean, modern, and trustworthy style
A subtle but creative watermark or graphic detail on the letterhead (not too invasive)

The same visual "family feeling" across business card, envelope, and letterhead: designs must be different but clearly connected

Strong readability for all text and contact details

Use our brand colors (Navy Blue, Green, Orange/Red) in a smart, non-overloaded way

No strict limitations: we are open to creative proposals as long as they are coherent, elegant, and suitable for professional use

Technical specifications:
100% full A4 page layout (no accidental borders)

Deliver ready-to-print PDFs and vector files (AI, EPS)

Respect 5 mm safety margins

Standard sizes for A4, business card, envelope C6 with window at the right

Tone:
Modern – Clean – Elegant – Creative – Trustworthy

Target Market(s)

Professional businesses, property managers, condominium administrators, companies, clinics, and offices requiring cleaning, gardening, and pest control services. The design must convey trust, reliability, professionalism, and attention to detail.

Industry/Entity Type

Cleaning Services, Gardening Services, Pest Control Services

Colors
0054AA
0677BA
7BADD7
CADEEF
E8F1F8
59FF00
82FF00
B8FF75
E3FFCB
F4FFEA
EB3D1F
EC4F4E
F09395
F8D3D4
FCEDEE

Requirements
Must have
• Cohesive design across business card, letterhead, and envelope Clean, modern, professional look Use of brand colors: Navy Blue (main), Green, Orange/Red accents Letterhead must include a subtle watermark without interfering with text Envelope must be with a transparent window for recipient address visibility High readability of all text and contact details Proper alignment, no unnecessary margins (full A4 layout)
Nice to have
• Creative but discreet use of the checkmark from the logo as part of the background or watermark Slight variation or accent of color tones while respecting brand identity A clean visual accent that gives a sense of movement or dynamic professionalism (without being distracting) Icons for email, phone, and website on the business card (if stylistically appropriate)
Should not have
• Overuse of colors or rainbow effects Heavy backgrounds or complex textures that interfere with readability Fonts that are too playful, comic-style, or non-professional Overcrowded layouts — the design must feel clean and spacious Watermarks that are too strong or central (they must be subtle and marginal)

```html
<!DOCTYPE html>
<html lang="en">
<head>
<meta charset="utf-8">
<title>Merida Care – Corporate Identity Pack</title>
<link rel="stylesheet" href="https://fonts.googleapis.com/css2?family=Montserrat:wght@600&family=Roboto:wght@400;500;700&family=Playfair+Display:ital,wght@1,700&display=swap">
<style>
:root{
  --orange:#f06a22;
  --green:#6cbd45;
  --navy:#27286b;
  --ink:#1f1f3d;
  --paper:#ffffff;
  --stage:#d5dcde;
  --window:#eef2f4;
  --caption:#f4f6f7;
}
*{margin:0;padding:0;box-sizing:border-box}
html,body{width:1200px;height:679px;overflow:hidden}
body{background:var(--stage);font-family:"Roboto",Arial,sans-serif;color:var(--ink);position:relative}
.piece{position:absolute;background:var(--paper);overflow:hidden}
.brand-name{position:absolute;font-family:"Montserrat",Arial,sans-serif;font-weight:600;color:var(--navy);letter-spacing:.04em;white-space:nowrap;display:flex;align-items:center;gap:.35em;line-height:1}
.brand-name .mark{display:inline-block;width:.9em;height:.9em;background:currentColor}
.band{position:absolute;left:0;bottom:0;width:100%}
.icon{width:7px;height:7px;display:inline-block;vertical-align:middle}
.tag{display:inline-block;font-size:4px;line-height:4px;border:0.6px solid var(--orange);color:var(--orange);border-radius:3px;padding:0 1px;vertical-align:middle}
.tick{color:var(--green);font-weight:700;margin-right:2px}

/* business card front */
.card-front{left:63px;top:214px;width:298px;height:170px}
.card-front .pattern{position:absolute;inset:0;background:linear-gradient(90deg,#ee6a22 0%,#f27a22 60%,#f6a424 100%)}
.card-front .front-name{left:40px;top:71px;font-size:23px;color:#fff}

/* business card back */
.card-back{left:63px;top:400px;width:298px;height:170px}
.card-back .back-head{left:0;right:0;top:16px;justify-content:center;font-size:16px}
.card-back .contacts{position:absolute;right:170px;top:71px;text-align:right;font-size:7px;line-height:9.6px}
.card-back .contacts .icon,.card-back .contacts .tag{margin-left:4px}
.card-back .divider{position:absolute;left:149px;top:56px;width:1px;height:80px;background:var(--orange)}
.card-back .company{position:absolute;left:160px;top:58px;font-size:7px;line-height:9.6px}
.card-back .company h2{font-size:10.5px;color:var(--orange);font-weight:700;margin-bottom:3px}
.card-back .company .green{color:var(--green);font-weight:500}
.card-back .band{height:36px}
.card-back .back-foot{left:0;right:0;top:140px;justify-content:center;font-size:8px}

/* letterhead */
.letterhead{left:394px;top:105px;width:330px;height:465px}
.letterhead .sheet-head{left:17px;top:22px;font-size:16px}
.letterhead .contacts{position:absolute;right:17px;top:17px;text-align:right;font-size:6px;line-height:8.6px}
.letterhead .contacts .icon,.letterhead .contacts .tag{margin-left:4px}
.letterhead .watermark{position:absolute;left:0;right:0;top:205px;text-align:center;font-family:"Montserrat",Arial,sans-serif;font-weight:600;font-size:40px;color:#eef5e8;letter-spacing:.04em}
.letterhead .band{height:78px}
.letterhead .sheet-foot{left:0;right:0;top:393px;justify-content:center;font-size:11px}
.letterhead .footer{position:absolute;left:0;right:0;top:426px;color:#fff;font-size:6px;line-height:8.4px}
.letterhead .footer h2{text-align:center;font-size:9.5px;line-height:10px;font-weight:500;margin-bottom:3px}
.letterhead .footer .cols{display:flex;gap:16px;padding-left:17px}
.letterhead .footer .tick{color:#8fd06a}

/* envelope front */
.envelope-front{left:756px;top:113px;width:374px;height:212px}
.envelope-front .env-head{right:12px;top:24px;font-size:18px}
.envelope-front .env-small{left:13px;top:87px;font-size:11px}
.envelope-front .contacts{position:absolute;left:12px;top:108px;font-size:8.5px;line-height:12.2px}
.envelope-front .contacts .icon,.envelope-front .contacts .tag{margin-right:6px}
.envelope-front .contacts .icon{width:8px;height:8px}
.envelope-front .window{position:absolute;left:193px;top:99px;width:150px;height:87px;background:var(--window)}
.envelope-front .band{height:36px}

/* envelope back */
.envelope-back{left:761px;top:357px;width:370px;height:213px}
.envelope-back .flap{position:absolute;left:4px;top:0;width:362px;height:67px;background:#fff;border-radius:0 0 14px 14px;box-shadow:0 6px 10px rgba(0,0,0,.12)}
.envelope-back .flap-name{left:0;right:0;top:24px;justify-content:center;font-size:14px;color:var(--green)}

/* captions */
.caption{position:absolute;font-family:"Playfair Display",Georgia,serif;font-style:italic;font-weight:700;color:var(--caption);text-align:center;letter-spacing:.04em;text-shadow:0 1px 2px rgba(0,0,0,.18)}
.caption-card{left:63px;width:298px;top:598px;font-size:32px}
.caption-letterhead{left:394px;width:330px;top:592px;font-size:32px}
.caption-envelope{left:756px;width:374px;top:596px;font-size:27px;line-height:31px}
</style>
</head>
<body>

<svg width="0" height="0" style="position:absolute">
  <defs>
    <symbol id="i-phone" viewBox="0 0 10 10"><path d="M2.2 .6l1.6 2-1 1.1a6 6 0 0 0 3.5 3.5l1.1-1 2 1.6-1 1.6C5 9.5.5 5 .6 1.6z" fill="#f06a22"/></symbol>
    <symbol id="i-at" viewBox="0 0 10 10"><text x="5" y="8.3" text-anchor="middle" font-size="10" font-family="Arial" font-weight="700" fill="#f06a22">@</text></symbol>
    <symbol id="i-globe" viewBox="0 0 10 10"><circle cx="5" cy="5" r="4.3" fill="none" stroke="#f06a22" stroke-width="1.2"/><ellipse cx="5" cy="5" rx="1.8" ry="4.3" fill="none" stroke="#f06a22" stroke-width="1"/><path d="M.7 5h8.6" stroke="#f06a22" stroke-width="1"/></symbol>
  </defs>
</svg>

<!-- Business card front -->
<section class="piece card-front" aria-label="Business card front">
  <div class="pattern" role="img" aria-label="Orange background with a repeating pattern of small tick boxes"></div>
  <div class="brand-name front-name"><span class="mark"></span>MERIDA CARE</div>
</section>

<!-- Business card back -->
<section class="piece card-back" aria-label="Business card back">
  <div class="brand-name back-head">MERIDA CARE</div>
  <div class="contacts">
    +39 333 1204578<svg class="icon"><use href="#i-phone"/></svg><br>
    office@merida-care.srl<svg class="icon"><use href="#i-at"/></svg><br>
    www.merida-care.srl<svg class="icon"><use href="#i-globe"/></svg><br>
    info.meridacare@pec.it<span class="tag">PEC</span><br>
    K7TQWN4<span class="tag">SDI</span>
  </div>
  <div class="divider"></div>
  <div class="company">
    <h2>Merida Care srl</h2>
    <div class="green"><span class="tick">✓</span>Società unipersonale</div>
    <div class="green"><span class="tick">✓</span>Einzelunternehmen</div>
    <div><span class="tick">✓</span>Via dei Castagni - Kastanienweg 9</div>
    <div><span class="tick">✓</span>I-39099 Valfiore-Blumental (Bz)</div>
    <div><span class="tick">✓</span>REA - VWV Nr. Bz 571203</div>
    <div><span class="tick">✓</span>P.I .- MwSt. 01847365928</div>
  </div>
  <svg class="band" viewBox="0 0 298 36" preserveAspectRatio="none">
    <path d="M0 0 Q149 52 298 0 V36 H0 Z" fill="#f06a22"/>
    <path d="M12 1 Q149 44 286 0" fill="none" stroke="#6cbd45" stroke-width="2.2"/>
  </svg>
  <div class="brand-name back-foot">MERIDA CARE</div>
</section>

<!-- A4 letterhead -->
<section class="piece letterhead" aria-label="A4 letterhead">
  <div class="brand-name sheet-head">MERIDA CARE</div>
  <div class="contacts">
    +39 333 1204578<svg class="icon"><use href="#i-phone"/></svg><br>
    office@merida-care.srl<svg class="icon"><use href="#i-at"/></svg><br>
    www.merida-care.srl<svg class="icon"><use href="#i-globe"/></svg><br>
    info.meridacare@pec.it<span class="tag">PEC</span><br>
    K7TQWN4<span class="tag">SDI</span>
  </div>
  <div class="watermark">MERIDA CARE</div>
  <svg class="band" viewBox="0 0 330 78" preserveAspectRatio="none">
    <path d="M0 6 Q165 66 330 6 V78 H0 Z" fill="#f06a22"/>
    <path d="M12 6 Q165 58 318 4" fill="none" stroke="#6cbd45" stroke-width="2.4"/>
  </svg>
  <div class="brand-name sheet-foot">MERIDA CARE</div>
  <div class="footer">
    <h2>Merida Care srl</h2>
    <div class="cols">
      <div><span class="tick">✓</span>Società unipersonale<br><span class="tick">✓</span>Einzelunternehmen</div>
      <div><span class="tick">✓</span>REA - VWV Nr. Bz 571203<br><span class="tick">✓</span>P.I .- MwSt. 01847365928</div>
      <div><span class="tick">✓</span>Via dei Castagni - Kastanienweg 9<br><span class="tick">✓</span>I-39099 Valfiore-Blumental (Bz)</div>
    </div>
  </div>
</section>

<!-- Envelope front -->
<section class="piece envelope-front" aria-label="Envelope front with recipient window">
  <div class="brand-name env-head">MERIDA CARE</div>
  <div class="brand-name env-small">MERIDA CARE</div>
  <div class="contacts">
    <svg class="icon"><use href="#i-phone"/></svg>+39 333 1204578<br>
    <svg class="icon"><use href="#i-at"/></svg>office@merida-care.srl<br>
    <svg class="icon"><use href="#i-globe"/></svg>www.merida-care.srl<br>
    <span class="tag">PEC</span>info.meridacare@pec.it<br>
    <span class="tag">SDI</span>K7TQWN4
  </div>
  <div class="window"></div>
  <svg class="band" viewBox="0 0 374 36" preserveAspectRatio="none">
    <path d="M0 2 Q187 62 374 2 V36 H0 Z" fill="#f06a22"/>
    <path d="M12 2 Q187 54 362 0" fill="none" stroke="#6cbd45" stroke-width="2.4"/>
  </svg>
</section>

<!-- Envelope back -->
<section class="piece envelope-back" aria-label="Envelope back">
  <div class="flap"><div class="brand-name flap-name">MERIDA CARE</div></div>
</section>

<div class="caption caption-card">Business Card</div>
<div class="caption caption-letterhead">A4 Letterhead</div>
<div class="caption caption-envelope">Envelope with recipient<br>window (C5 size)</div>

</body>
</html>
```